Business Card Design

I need a business card design for a new company based in Sydney called 'The Brisk Ladle'. We deliver organic, gourmet and fine foods to your door.

I would like to see creative, unique designs which use colours which represent health and nature like green.

Target Market(s)

Health conscious 20 to 35 year olds.

Industry/Entity Type

Health

Contact Information for Business Card

The Brisk Ladle, Owen Pardalis, owen@thebriskladle.com.au, 0427865193

Requirements
Must have
• My logo.

```html
<!DOCTYPE html>
<html lang="en">
<head>
<meta charset="utf-8">
<title>The Brisk Ladle — Business Card</title>
<link href="https://fonts.googleapis.com/css2?family=Jost:wght@300;400&family=Open+Sans:wght@400;700&display=swap" rel="stylesheet">
<style>
  :root {
    --page: #ffffff;
    --front-top: #fbfdf9;
    --front-bottom: #f1f6ec;
    --brand-green: #5db92c;
    --deep-green: #3d8f1f;
    --lime: #8ee21a;
    --leaf: #b4f02a;
    --ink: #333333;
    --card-border: #a9a9a9;
  }
  html, body {
    margin: 0;
    padding: 0;
    width: 989px;
    height: 1200px;
    overflow: hidden;
    background: var(--page);
  }
  .sheet {
    position: relative;
    width: 989px;
    height: 1200px;
  }
  .card {
    position: absolute;
    box-sizing: border-box;
  }
  .card--front {
    left: 77px;
    top: 77px;
    width: 820px;
    height: 452px;
    background: linear-gradient(180deg, var(--front-top) 0%, var(--front-bottom) 100%);
  }
  .brand {
    position: absolute;
    left: 236px;
    top: 190px;
    display: flex;
    align-items: center;
    gap: 22px;
  }
  .brand__dot {
    width: 118px;
    height: 118px;
    border-radius: 50%;
    background: var(--brand-green);
    flex: none;
  }
  .brand__name {
    margin: 0;
    font-family: "Jost", sans-serif;
    font-weight: 300;
    font-size: 66px;
    line-height: 0.95;
    color: var(--brand-green);
    letter-spacing: 0.5px;
  }
  .card--back {
    left: 75px;
    top: 607px;
    width: 833px;
    height: 508px;
    background: #fff;
    border: 1px solid var(--card-border);
    overflow: hidden;
  }
  .card__art {
    position: absolute;
    left: 0;
    top: 0;
    width: 380px;
    height: 100%;
    background: linear-gradient(160deg, var(--deep-green) 0%, var(--lime) 45%, var(--leaf) 100%);
  }
  .contact {
    position: absolute;
    right: 63px;
    top: 153px;
    text-align: right;
  }
  .contact__name {
    margin: 0;
    font-family: "Jost", sans-serif;
    font-weight: 300;
    font-size: 42px;
    line-height: 1.1;
    color: var(--deep-green);
  }
  .contact__email {
    margin: 4px 0 0;
    font-family: "Open Sans", sans-serif;
    font-size: 24px;
    color: var(--ink);
  }
  .contact__phone {
    margin: 38px 0 0;
    display: flex;
    justify-content: flex-end;
    align-items: center;
    gap: 16px;
    font-family: "Open Sans", sans-serif;
    font-weight: 700;
    font-size: 31px;
    color: var(--ink);
  }
  .contact__icon {
    width: 40px;
    height: 40px;
  }
</style>
</head>
<body>
<div class="sheet">
  <section class="card card--front">
    <div class="brand">
      <span class="brand__dot"></span>
      <p class="brand__name">The Brisk<br>Ladle</p>
    </div>
  </section>

  <section class="card card--back">
    <div class="card__art" role="img" aria-label="Large green brand emblem decoration"></div>
    <div class="contact">
      <p class="contact__name">Owen Pardalis</p>
      <p class="contact__email">owen@thebriskladle.com.au</p>
      <p class="contact__phone">
        <svg class="contact__icon" viewBox="0 0 40 40" aria-hidden="true">
          <circle cx="20" cy="20" r="17.5" fill="none" stroke="var(--brand-green)" stroke-width="3"/>
          <path d="M15 11c-2 1-3 3-2.5 6 .8 5 5 10 9.5 12 2.5 1 4.5.5 5.5-1l-3.5-3.5-2.5 1.2c-2-1.2-3.6-3.5-4.3-5.7l2.2-1.6L18 12z" fill="var(--brand-green)"/>
        </svg>
        <span>0427 865 193</span>
      </p>
    </div>
  </section>
</div>
</body>
</html>
```